Business card design

We need a business card designed completed for a new company. We are a company that works with associations, schools to convert their older text/DVDs into dynamic online and mobile programs. Our initial platform is designed for the legal associations and will enable their lawyers to access their content such as forms, videos, case law and support materials anywhere, anytime. We are also focused on Project Management Associations, Financial Management Associations and IT Associations.

I would like for the business card to have the following information:

Logo

Gavin tremblor

President and CEO

gtremblor@learnquay.example

Mobile: 613-547-3916

www.learnquay.example

Tag line: Transforming content into a mobile platform    

I would like it to be double sided, use the colours of the logo, tie into the mobile world

 

Industry/Entity Type

Legal

Logo Text

Learnquay

```html
<!DOCTYPE html>
<html lang="en">
<head>
<meta charset="utf-8">
<title>Learnquay business card</title>
<link rel="stylesheet" href="https://fonts.googleapis.com/css2?family=Open+Sans:ital,wght@0,400;0,600;1,400&family=Tinos&display=swap">
<style>
  :root {
    --page: #e4e4e4;
    --card-black: #0d0d0d;
    --card-black-edge: #262626;
    --card-grey: #a9a9a9;
    --card-grey-light: #bdbdbd;
    --mark-square: #9a9a9a;
    --white: #ffffff;
    --text-soft: #c9c9c9;
    --text-muted: #9c9c9c;
  }
  * { box-sizing: border-box; margin: 0; padding: 0; }
  html, body { width: 1200px; height: 976px; overflow: hidden; }
  body {
    background: var(--page);
    font-family: "Open Sans", Arial, sans-serif;
    display: flex;
    flex-direction: column;
    align-items: center;
    justify-content: center;
    gap: 56px;
  }
  .card {
    position: relative;
    width: 700px;
    height: 400px;
    border-radius: 22px;
    overflow: hidden;
    box-shadow: 0 10px 24px rgba(0,0,0,.25);
  }

  /* shared brand name: one colour, one weight, plain square beside */
  .brand {
    display: flex;
    align-items: center;
    gap: 14px;
    color: var(--white);
    font-weight: 600;
    line-height: 1;
  }
  .brand__square {
    flex: none;
    background: var(--mark-square);
  }

  /* back side */
  .card--back {
    background: linear-gradient(160deg, var(--card-grey-light), var(--card-grey) 60%);
  }
  .card--back .wave-field {
    position: absolute;
    right: 0; top: 0;
    width: 300px; height: 240px;
    background: radial-gradient(ellipse at 80% 30%, rgba(255,255,255,.22), rgba(255,255,255,0) 70%);
  }
  .card--back .brand {
    position: absolute;
    left: 0; right: 0; top: 0; bottom: 0;
    justify-content: center;
    font-size: 64px;
  }
  .card--back .brand__square {
    width: 44px; height: 44px;
    background: var(--white);
    opacity: .55;
  }

  /* front side */
  .card--front {
    background: linear-gradient(170deg, var(--card-black-edge), var(--card-black) 45%);
    color: var(--white);
  }
  .card--front .wave-field {
    position: absolute;
    right: 0; bottom: 0;
    width: 460px; height: 200px;
    background: radial-gradient(ellipse at 60% 90%, rgba(255,255,255,.16), rgba(255,255,255,0) 70%);
  }
  .card--front .brand {
    position: absolute;
    left: 60px; top: 86px;
    font-size: 40px;
  }
  .card--front .brand__square {
    width: 30px; height: 30px;
  }
  .tagline {
    position: absolute;
    left: 60px; top: 148px;
    font-style: italic;
    font-size: 15px;
    color: var(--text-soft);
  }
  .person {
    position: absolute;
    left: 60px; top: 248px;
  }
  .person__name {
    font-family: "Tinos", "Times New Roman", serif;
    font-size: 40px;
    line-height: 1.1;
  }
  .person__role {
    font-size: 17px;
    color: var(--text-muted);
    margin-top: 4px;
  }
  .contact {
    position: absolute;
    left: 440px; top: 72px;
    padding-left: 16px;
    border-left: 2px solid var(--white);
    font-size: 14px;
    line-height: 1.75;
    color: var(--text-soft);
  }
</style>
</head>
<body>

  <section class="card card--back" aria-label="Card back">
    <div class="wave-field" role="img" aria-label="Soft flowing line pattern"></div>
    <div class="brand"><span class="brand__square"></span><span class="brand__name">Learnquay</span></div>
  </section>

  <section class="card card--front" aria-label="Card front">
    <div class="wave-field" role="img" aria-label="Soft flowing line pattern"></div>
    <div class="brand"><span class="brand__square"></span><span class="brand__name">Learnquay</span></div>
    <p class="tagline">Transforming content into a mobile platform</p>
    <div class="person">
      <p class="person__name">Gavin tremblor</p>
      <p class="person__role">President and CEO</p>
    </div>
    <div class="contact">
      <p>gtremblor@learnquay.example</p>
      <p>Mobile: 613-547-3916</p>
      <p>www.learnquay.example</p>
    </div>
  </section>

</body>
</html>
```